Energy drink company looking for a complete can design

Design an energy drink can label using an established trademarked logo along with mandatory nutrition and ingredients table.
We would like to see 3 versions or samples to judge:
1. can design over a black background - called dark color version
2. can design over a white background - called light color version
3. can design over a grey/silver background - called balanced color version

Target Market(s)

USA

Requirements
Must have
• the phrase "yes kelvora energy drink" "yes kelvora" and "ALL Natural Libido Enhancing energy drink" must be on the can somewhere

```html
<!DOCTYPE html>
<html lang="en">
<head>
<meta charset="UTF-8">
<title>yes kelvora energy drink – can label, balanced colour version</title>
<link href="https://fonts.googleapis.com/css2?family=Archivo:wght@400;600;700;800;900&family=Open+Sans:wght@400;600&display=swap" rel="stylesheet">
<style>
  :root{
    --silver-light:#f6f6f6;
    --silver-mid:#dcdcdc;
    --silver-dark:#bdbdbd;
    --ink:#111111;
    --navy:#1b2030;
    --gold:#f2c200;
    --orange:#e8801c;
    --fruit-light:#ffe27a;
    --fruit-deep:#f0a81c;
  }
  *{box-sizing:border-box;margin:0;padding:0}
  html,body{width:1200px;height:846px;overflow:hidden}
  body{background:#ffffff}
  .label{
    position:relative;width:1200px;height:846px;overflow:hidden;
    background:linear-gradient(90deg,var(--silver-dark) 0%,var(--silver-light) 30%,var(--silver-mid) 48%,var(--silver-light) 62%,var(--silver-mid) 100%);
    font-family:"Archivo",Arial,sans-serif;color:var(--ink);
  }
  .fruit{position:absolute;border-radius:50%;
    background:radial-gradient(circle at 45% 45%,var(--fruit-light) 0%,var(--fruit-deep) 55%,rgba(240,168,28,0) 72%)}
  .fruit--top{left:380px;top:-120px;width:300px;height:200px}
  .fruit--top-right{left:880px;top:-60px;width:130px;height:100px}
  .fruit--bottom-left{left:-90px;top:640px;width:340px;height:300px}
  .fruit--bottom-mid{left:300px;top:700px;width:300px;height:240px}
  .fruit--bottom-right{left:990px;top:650px;width:320px;height:300px}

  .hero-art{
    position:absolute;left:156px;top:72px;width:240px;height:426px;border-radius:46% 46% 42% 42%;
    background:radial-gradient(ellipse at 50% 55%,#ffd24a 0%,#f2a623 45%,#c97a12 70%,rgba(201,122,18,0) 72%);
  }
  .brand-name{
    position:absolute;left:44px;top:500px;width:380px;text-align:center;
    font-weight:800;font-size:54px;line-height:62px;letter-spacing:-1px;color:var(--orange);
  }
  .tagline{
    position:absolute;left:117px;top:658px;width:234px;text-align:center;
    font-weight:700;font-size:13px;line-height:17px;color:var(--ink);letter-spacing:.2px;
  }
  .vertical{position:absolute;transform:translate(-50%,-50%) rotate(-90deg);white-space:nowrap;font-weight:800;line-height:1}
  .vertical--full{left:596px;top:432px;font-size:46px;color:var(--navy)}
  .vertical--short{left:1088px;top:294px;font-size:50px;color:var(--gold)}

  .nutrition{
    position:absolute;left:730px;top:42px;width:240px;height:542px;
    background:#ffffff;border:1px solid var(--ink);padding:2px 4px;font-size:10.5px;
    display:flex;flex-direction:column;
  }
  .nutrition__title{font-weight:900;font-size:27px;line-height:30px;letter-spacing:-.5px}
  .nutrition__serving{display:flex;justify-content:space-between;font-weight:700;font-size:12px;height:16px}
  .bar-thick{height:10px;background:var(--ink);margin:1px 0}
  .bar-mid{height:5px;background:var(--ink)}
  .bar-heavy{height:7px;background:var(--ink)}
  .bar-thin{height:3px;background:var(--ink)}
  .nutrition__amount{font-weight:700;font-size:9.5px;height:13px;line-height:13px}
  .nutrition__calories{display:flex;justify-content:space-between;align-items:flex-end;height:25px;font-weight:900}
  .nutrition__calories span:first-child{font-size:20px}
  .nutrition__calories span:last-child{font-size:29px;line-height:29px}
  .nutrition__dv{text-align:right;font-weight:700;font-size:9.5px;height:15px;line-height:15px;border-bottom:1px solid var(--ink)}
  .row{display:flex;justify-content:space-between;align-items:center;height:18.2px;border-bottom:1px solid #555}
  .row b{font-weight:800}
  .row--indent{padding-left:12px}
  .row--indent2{padding-left:24px}
  .row--vit{height:18.4px;font-weight:400}
  .row--last{border-bottom:none}
  .nutrition__note{font-size:7.2px;line-height:8.8px;padding-top:2px}

  .info{position:absolute;left:600px;top:596px;width:534px;font-family:"Open Sans",Arial,sans-serif;font-size:14px;line-height:21px;color:var(--ink)}
  .info__row{display:flex}
  .info__label{width:124px;text-align:right;padding-right:6px;flex:none;font-weight:600}
  .info__text{flex:1}
</style>
</head>
<body>
<main class="label">
  <div class="fruit fruit--top" role="img" aria-label="Pineapple slices and juice splash photo"></div>
  <div class="fruit fruit--top-right" role="img" aria-label="Pineapple slice photo"></div>
  <div class="fruit fruit--bottom-left" role="img" aria-label="Pineapple slices photo"></div>
  <div class="fruit fruit--bottom-mid" role="img" aria-label="Pineapple slices photo"></div>
  <div class="fruit fruit--bottom-right" role="img" aria-label="Pineapple slices photo"></div>

  <div class="hero-art" role="img" aria-label="Illustration of a halved pineapple with juice splash"></div>
  <div class="brand-name">yes kelvora</div>
  <p class="tagline">ALL NATURAL LIBIDO<br>ENHANCING ENERGY DRINK</p>

  <div class="vertical vertical--full">yes kelvora energy drink</div>
  <div class="vertical vertical--short">yes kelvora</div>

  <section class="nutrition">
    <div class="nutrition__title">Nutrition Facts</div>
    <div class="nutrition__serving"><span>Serving size</span><span>12 fl oz (355 mL)</span></div>
    <div class="bar-thick"></div>
    <div class="nutrition__amount">Amount per serving</div>
    <div class="nutrition__calories"><span>Calories</span><span>90</span></div>
    <div class="bar-mid"></div>
    <div class="nutrition__dv">% Daily Value*</div>
    <div class="row"><span><b>Total Fat</b> 0g</span><b>0%</b></div>
    <div class="row row--indent"><span>Saturated Fat 0g</span><b>0%</b></div>
    <div class="row row--indent"><span>Trans Fat 0g</span><span></span></div>
    <div class="row"><span><b>Cholesterol</b> 0mg</span><b>0%</b></div>
    <div class="row"><span><b>Sodium</b> 5mg</span><b>0%</b></div>
    <div class="row"><span><b>Total Carbohydrate</b> 21g</span><b>8%</b></div>
    <div class="row row--indent"><span>Dietary Fiber 0g</span><b>0%</b></div>
    <div class="row row--indent"><span>Total Sugars 18g</span><span></span></div>
    <div class="row row--indent2"><span>Includes 0g Added Sugars</span><b>0%</b></div>
    <div class="row row--last"><span><b>Protein</b> 0g</span><span></span></div>
    <div class="bar-heavy"></div>
    <div class="row row--vit"><span>Vitamin D 0mcg</span><span>0%</span></div>
    <div class="row row--vit"><span>Calcium 16mg</span><span>2%</span></div>
    <div class="row row--vit"><span>Iron 0mg</span><span>0%</span></div>
    <div class="row row--vit"><span>Potassium 238mg</span><span>6%</span></div>
    <div class="row row--vit"><span>Vitamin C 138mg</span><span>150%</span></div>
    <div class="row row--vit"><span>Niacin 24mg</span><span>150%</span></div>
    <div class="row row--vit"><span>Vitamin B<sub>6</sub> 2.6mg</span><span>150%</span></div>
    <div class="row row--vit"><span>Vitamin B<sub>12</sub> 3.6mcg</span><span>150%</span></div>
    <div class="row row--vit"><span>Pantothenic Acid 7mg</span><span>140%</span></div>
    <div class="row row--vit row--last"><span>Zinc 6mg</span><span>50%</span></div>
    <div class="bar-thin"></div>
    <p class="nutrition__note">*The % Daily Value tells you how much a nutrient in a serving of food contributes to a daily diet. 2,000 calories a day is used for general nutrition advice.</p>
  </section>

  <section class="info">
    <div class="info__row"><span class="info__label">Allergens:</span><span class="info__text">None</span></div>
    <div class="info__row"><span class="info__label">Ingredients:</span><span class="info__text">Filtered Water, Organic Peach Juice Concentrate, Organic White Grape Juice Concentrate, Organic Pear Juice Concentrate, Organic Pineapple Juice Concentrate, Organic Natural Flavors, Horny Goat Weed Extract, Citric Acid, L-Arginine, Taurine, Maca Root Extract, Ascorbic Acid, Natural Caffeine from Green Tea, Panax Ginseng, Organic Monk Fruit, Gingko Biloba, Stevia Reb M, Niacinamide, Zinc Citrate, Calcium Pantothenate, Pyridoxine Hydrochloride, Cyanocobalamin</span></div>
  </section>
</main>
</body>
</html>
```